Healing Arts Brochure with Simple, Elegant, Zen Design ,

I need to create a brochure for an upcoming event and I have to complete this project in the next few days.
I would like a tri-fold or z fold type of brochure- standard size of 8.5 x 11- both sides with text

i would like the overall design to be simple, elegant and zen .... yet not too plain :-))
I would like the fonts used to be clean and clear and ... easy to read.
I would like the background color to be white/cream or light color
Please do not use too many colors when working with the descriptions of my services or break those sections up too much ... a little is ok.
I don't want the brochure to be busy

I've uploaded the text, my photo, a photo that I will be using on my website, my logo symbol without my name and several logo symbols with my name in different font styles. I am not wed to any of the various font styles of the logo just yet.
TEXT FILE IS UPLOADED
Updates

Dear Designers, The design submissions that I'm receiving so far have not been including all 3 pages of text in the brochure. I pulled my text file to update it with the instructions that there are 3 pages of text information that need to be on the brochure. Unfortunately, I'm not able to upload the text file - seems to be a glitch on the PixelTorch website.. I called for support and they won't get back to me for a couple of hours. That will be around 11:00 am PST in the USA. PLEASE CHECK BACK if you haven't already downloaded the text file. Otherwise, please add the missing information and resubmit your ideas. Thank you!! RM

Target Market(s)

My services target clients in the healing arts.

Industry/Entity Type

Event

Requirements
Must have
• Please include the colors tones of my logo and the sunset photo -golds, oranges, blues
Brochure must include my photo and the sunset photo
Should not have
• Objects like teacups etc. that have nothing to do with my services - thank you kindly
I don't want any other photos or objects on the brochure other than my photo and the sun
Please don't put the tagline in quotes
Please do not make the brochure busy with too many colors in the text.

```html
<!DOCTYPE html>
<html lang="en">
<head>
<meta charset="utf-8">
<title>Rowan Mirelle — Healing Arts Brochure Panel</title>
<link rel="stylesheet" href="https://fonts.googleapis.com/css2?family=Arimo:wght@400;700&display=swap">
<style>
  :root {
    --cream: #fdfbef;
    --gold: #fcc63a;
    --gold-light: #ffd85a;
    --orange: #f29a2e;
    --orange-deep: #e8741f;
    --blue: #3e68b2;
    --ink: #2b2b2b;
    --white: #ffffff;
  }
  * { margin: 0; padding: 0; box-sizing: border-box; }
  html, body { width: 1000px; height: 1200px; overflow: hidden; background: var(--cream); }
  body { font-family: "Arimo", Helvetica, Arial, sans-serif; color: var(--ink); }

  .brochure { position: relative; width: 1000px; height: 1200px; overflow: hidden; }
  .backdrop { position: absolute; inset: 0; }

  .intro {
    position: absolute; left: 110px; top: 42px; width: 390px;
    font-size: 26.6px; line-height: 29.6px; white-space: nowrap;
  }
  .section-heading {
    position: absolute; left: 35px;
    font-size: 25px; font-weight: 700; color: var(--blue);
    line-height: 27px; padding: 2px 60px 2px 8px; white-space: nowrap;
    background: linear-gradient(90deg, var(--gold) 0%, var(--gold) 45%, rgba(252,198,58,0) 100%);
  }
  .services-heading { top: 370px; width: 265px; }
  .symptoms-heading { top: 774px; width: 430px; }
  .services-text {
    position: absolute; left: 35px; top: 415px; width: 460px;
    font-size: 26.6px; line-height: 29.6px; white-space: nowrap;
  }
  .symptom-list {
    position: absolute; left: 35px; top: 848px; width: 460px;
    list-style: none; font-size: 26.6px; line-height: 29.6px; white-space: nowrap;
  }
  .symptom-list li { position: relative; padding-left: 34px; }
  .symptom-list li::before {
    content: ""; position: absolute; left: 2px; top: 13px;
    width: 6px; height: 6px; border-radius: 50%; background: var(--ink);
  }

  .practitioner-name {
    position: absolute; left: 700px; top: 439px; width: 290px; text-align: center;
    font-size: 22px; font-weight: 700; color: #1e1e1e; line-height: 26px; white-space: nowrap;
  }
  .practitioner-credentials {
    position: absolute; left: 700px; top: 466px; width: 290px; text-align: center;
    font-size: 20px; color: #1e1e1e; white-space: nowrap;
  }
  .tagline {
    position: absolute; left: 596px; top: 578px; width: 400px;
    font-size: 57px; line-height: 62.5px; color: var(--white); white-space: nowrap;
  }
  .brand-name {
    position: absolute; left: 820px; top: 1141px;
    font-size: 23px; line-height: 28px; color: var(--blue); font-weight: 400; white-space: nowrap;
  }
</style>
</head>
<body>
<main class="brochure">
  <svg class="backdrop" width="1000" height="1200" viewBox="0 0 1000 1200" xmlns="http://www.w3.org/2000/svg">
    <defs>
      <linearGradient id="sunset-tone" x1="0" y1="0" x2="0" y2="1">
        <stop offset="0" stop-color="#e9731c"/>
        <stop offset="0.35" stop-color="#f7a431"/>
        <stop offset="0.55" stop-color="#fbc04a"/>
        <stop offset="1" stop-color="#e58626"/>
      </linearGradient>
      <linearGradient id="panel-orange" x1="0" y1="0" x2="0" y2="1">
        <stop offset="0" stop-color="#fdc83c"/>
        <stop offset="0.55" stop-color="#f6a02f"/>
        <stop offset="1" stop-color="#ee7b22"/>
      </linearGradient>
      <linearGradient id="corner-gold" x1="0" y1="0" x2="1" y2="1">
        <stop offset="0" stop-color="#fdd046"/>
        <stop offset="1" stop-color="#f2a030"/>
      </linearGradient>
      <radialGradient id="portrait-tone" cx="0.5" cy="0.45" r="0.6">
        <stop offset="0" stop-color="#d9a98a"/>
        <stop offset="0.6" stop-color="#8a6a4c"/>
        <stop offset="1" stop-color="#2d3a22"/>
      </radialGradient>
      <radialGradient id="lotus-tone" cx="0.5" cy="0.5" r="0.5">
        <stop offset="0" stop-color="#d9dde8" stop-opacity="0.8"/>
        <stop offset="1" stop-color="#f6e6c2" stop-opacity="0"/>
      </radialGradient>
    </defs>

    <rect class="left-panel" x="0" y="0" width="510" height="1200" fill="var(--cream)"/>
    <ellipse class="lotus-motif" role="img" aria-label="Faint lotus flower motif" cx="420" cy="1030" rx="140" ry="110" fill="url(#lotus-tone)"/>
    <path class="corner-band-blue" d="M160,1200 C320,1140 440,1075 510,1005 L510,1200 Z" fill="var(--blue)"/>
    <path class="corner-band-gold" d="M190,1200 C345,1148 450,1090 510,1030 L510,1200 Z" fill="url(#corner-gold)"/>

    <rect class="sunset-photo" role="img" aria-label="Photo of a golden sunset over the ocean" x="510" y="0" width="490" height="340" fill="url(#sunset-tone)"/>
    <path class="header-band-blue" d="M510,310 C680,232 860,226 1000,298 L1000,330 C860,258 680,262 510,336 Z" fill="var(--blue)"/>
    <path class="header-band-orange" d="M510,326 C680,250 860,246 1000,316 L1000,336 C860,268 680,272 510,346 Z" fill="var(--orange-deep)"/>
    <path class="panel-body" d="M510,340 C680,266 860,262 1000,332 L1000,1200 L510,1200 Z" fill="url(#panel-orange)"/>

    <ellipse class="portrait-frame" cx="846" cy="285" rx="124" ry="137" fill="var(--orange)"/>
    <ellipse class="portrait-photo" role="img" aria-label="Portrait photo of the practitioner" cx="846" cy="285" rx="116" ry="129" fill="url(#portrait-tone)"/>

    <rect class="quote-mark" x="553" y="500" width="30" height="135" fill="var(--gold-light)"/>

    <path class="footer-band-blue" d="M620,1200 C810,1130 950,1040 1000,925 L1000,1200 Z" fill="var(--blue)"/>
    <path class="footer-band-white" d="M650,1200 C830,1135 955,1050 1000,952 L1000,1200 Z" fill="var(--white)"/>
    <path class="footer-band-orange" d="M668,1200 C845,1140 962,1058 1000,966 L1000,1200 Z" fill="#f39a35"/>

    <circle class="brand-mark" cx="800" cy="1155" r="16" fill="var(--orange-deep)"/>

    <rect class="drop-cap-bar" x="38" y="44" width="60" height="10" fill="var(--gold)"/>
    <rect class="drop-cap-stem" x="62" y="44" width="11" height="288" fill="var(--gold)"/>
  </svg>

  <p class="intro">he services that I offer focus<br>on supporting self-care,<br>self-empowerment and<br>self-regulation. Healing is<br>returning home to our inherent<br>sense of resiliency, vitality and<br>well-being. I am honored to<br>work with you and support<br>you in your own unique<br>journey home to yourself.</p>

  <h2 class="section-heading services-heading">Services:</h2>
  <p class="services-text">Somatic Experiencing is a body-<br>oriented appoach to resolving the<br>symptoms of trauma and chronic<br>stress. Sources of trauma are wide-<br>ranging, including; accident, falls,<br>surgeries, injuries, physical assault,<br>rape; emotional, physical or sexual<br>abuse; loss of loved one, childhood<br>neglect or abuse, difficult births,<br>high fever, serious illness, natural<br>disasters, violence and war.</p>

  <h2 class="section-heading symptoms-heading">The symptoms of unresolved<br>trauma can include:</h2>
  <ul class="symptom-list">
    <li>Panic or anxiety (including panic<br>attacks)</li>
    <li>Hyper-vigilance</li>
    <li>Chronic pain of all kinds</li>
    <li>Sleep disorders</li>
    <li>Chronic tension</li>
    <li>Addiction of all kinds</li>
    <li>Migraines</li>
  </ul>

  <p class="practitioner-name">ROWAN MIRELLE</p>
  <p class="practitioner-credentials">CMT, SEP</p>

  <p class="tagline">Offerings to<br>support you<br>in discovering<br>health,<br>resiliency and<br>well being</p>

  <p class="brand-name">Rowan Mirelle</p>
</main>
</body>
</html>
```